Fernhollow Estates Cards and Letterhead
EPS and PNG formatted logo files have been uploaded
Please feel free to post ideas for letterhead / stationary as well. Thanks.
SiteAdmin - I haven't yet received my logo files. If there is somewhere I can download them from please let me know. Thanks.
Attention Project Holder!!
Please be advised to upload your logo file in AI, EPS or PNG format so that the designers can incorporate your logo in this designs.
QT/PWF/HR Team
If you have the ability to create a couple of PowerPoint master slides based on the look and feel of the logo I'd be willing to pay extra for those. Thx.

```html
<!DOCTYPE html>
<html lang="en">
<head>
<meta charset="utf-8">
<title>Fernhollow Estates Business Card</title>
<link rel="stylesheet" href="https://fonts.googleapis.com/css2?family=Michroma&display=swap">
<style>
  :root {
    --page: #e9e9e6;
    --card: #ffffff;
    --navy: #2c3b78;
    --navy-text: #2c3b78;
    --strip: #c9ccd2;
    --band-text: #ffffff;
  }
  * { margin: 0; padding: 0; box-sizing: border-box; }
  html, body {
    width: 1200px; height: 900px; overflow: hidden;
    background: var(--page);
    font-family: "Michroma", sans-serif;
  }
  .card {
    position: absolute;
    left: 100px; top: 164px;
    width: 1000px; height: 572px;
    background: var(--card);
    box-shadow: 0 6px 18px rgba(0,0,0,0.12);
    overflow: hidden;
  }
  .brand {
    position: absolute;
    left: 150px; top: 92px;
    display: flex; align-items: flex-start; gap: 18px;
    color: var(--navy-text);
  }
  .brand-mark {
    width: 44px; height: 44px;
    background: var(--navy);
    margin-top: 4px;
  }
  .brand-name {
    font-size: 38px; line-height: 1.15;
    text-transform: uppercase;
    letter-spacing: 0.5px;
  }
  .brand-name .suffix {
    display: block; text-align: right;
  }
  .band {
    position: absolute;
    left: 0; top: 218px;
    width: 100%; height: 200px;
    background: var(--navy);
    color: var(--band-text);
  }
  .band-edge {
    position: absolute;
    left: 0; top: 418px;
    width: 100%; height: 14px;
    background: var(--strip);
  }
  .contact {
    position: absolute;
    left: 30px; top: 78px;
    list-style: none;
    font-size: 12.5px;
    letter-spacing: 1.5px;
    text-transform: uppercase;
  }
  .contact li {
    display: flex; align-items: center; gap: 10px;
    height: 21px;
  }
  .contact svg { width: 14px; height: 14px; flex: none; }
  .holder {
    position: absolute;
    right: 34px; top: 96px;
    text-align: right;
    text-transform: uppercase;
  }
  .holder-name { font-size: 19px; letter-spacing: 2px; }
  .holder-title { font-size: 13px; letter-spacing: 2px; margin-top: 14px; }
</style>
</head>
<body>
  <div class="card">
    <div class="brand">
      <span class="brand-mark"></span>
      <div class="brand-name">Fernhollow Estates<span class="suffix">LLC</span></div>
    </div>

    <div class="band">
      <ul class="contact">
        <li>
          <svg viewBox="0 0 14 14" aria-hidden="true"><circle cx="7" cy="7" r="7" fill="#fff"/><path d="M7 3.2a2.4 2.4 0 0 0-2.4 2.4C4.6 7.6 7 10.8 7 10.8s2.4-3.2 2.4-5.2A2.4 2.4 0 0 0 7 3.2z" fill="#2c3b78"/></svg>
          Suite # 214, Alder Row NY 5817
        </li>
        <li>
          <svg viewBox="0 0 14 14" aria-hidden="true"><circle cx="7" cy="7" r="7" fill="#fff"/><path d="M4.6 3.6l1.4 1.6-.7 1a5 5 0 0 0 2.5 2.5l1-.7 1.6 1.4-.8 1.2C7.4 10.4 3.6 6.6 3.4 4.4z" fill="#2c3b78"/></svg>
          207-555-0186
        </li>
        <li>
          <svg viewBox="0 0 14 14" aria-hidden="true"><circle cx="7" cy="7" r="7" fill="#fff"/><rect x="3.6" y="4.6" width="6.8" height="4.8" fill="none" stroke="#2c3b78" stroke-width="1"/><path d="M3.6 4.6L7 7.4l3.4-2.8" fill="none" stroke="#2c3b78" stroke-width="1"/></svg>
          rhys.villaine@fernhollowestatesllc.com
        </li>
        <li>
          <svg viewBox="0 0 14 14" aria-hidden="true"><circle cx="7" cy="7" r="7" fill="#fff"/><circle cx="7" cy="7" r="3.4" fill="none" stroke="#2c3b78" stroke-width="1"/><path d="M3.6 7h6.8M7 3.6v6.8" stroke="#2c3b78" stroke-width="0.8"/></svg>
          www.fernhollowestatesllc.com
        </li>
      </ul>
      <div class="holder">
        <div class="holder-name">Rhys Villaine</div>
        <div class="holder-title">TBD</div>
      </div>
    </div>
    <div class="band-edge"></div>
  </div>
</body>
</html>
```